Real Estate Design Website

I would like to have a design for "Harborline Realty" website. It needs to be in a "Responsive" framework.

The design need to be suitable for different viewer from all around the world. It needs to be modern. It'd be great if there is a design for mobile and tovix/tablet (it's all under responsive framework). It needs to be easy to navigate and look modern

Target Market(s)

End user/Real estate buyers from different part of the world

Industry/Entity Type

Real Estate

Requirements
Must have
• It's for Harborline Realty website which is used to represent their brand/image but at the same time it also for their client which is real estate buyers
Should not have
• Should not be boring design/out of date

```html
<!DOCTYPE html>
<html lang="en">
<head>
<meta charset="utf-8">
<title>Harborline Realty</title>
<link href="https://fonts.googleapis.com/css2?family=Open+Sans:wght@300;400;600&family=Questrial&display=swap" rel="stylesheet">
<style>
:root{
  --page:#e8e8e8;
  --white:#ffffff;
  --brand:#1477a8;
  --brand-dark:#0d6a99;
  --band:#127bab;
  --ink:#111111;
  --text:#6b6b6b;
  --nav:#333333;
  --search:#2b3a44;
}
*{box-sizing:border-box;margin:0;padding:0}
html,body{width:971px;height:1200px;overflow:hidden}
body{position:relative;background:var(--page);font-family:"Open Sans",Arial,sans-serif;color:var(--text)}
.abs{position:absolute}
.hero{left:0;top:0;width:971px;height:358px;
  background:linear-gradient(180deg,#4d9bd6 0%,#8cc3ea 32%,#a9b8c4 48%,#7c7a78 62%,#8a6f5c 72%,#3b6c8c 80%,#2c5f82 100%)}
.header{left:87px;top:0;width:797px;height:49px;background:var(--white)}
.logo{left:0;top:0;width:162px;height:49px;background:var(--brand);color:var(--white);
  font-family:"Questrial",sans-serif;font-size:15px;line-height:49px;padding-left:14px;letter-spacing:.3px}
.nav{right:137px;top:0;height:49px;display:flex;gap:20px;align-items:center;font-size:12.5px;color:var(--nav)}
.nav a{color:var(--nav);text-decoration:none}
.nav .current{color:var(--brand);border-bottom:1px solid var(--brand);padding-bottom:2px}
.btn{display:flex;height:29px;color:var(--white);font-family:"Questrial",sans-serif}
.btn .label{background:var(--brand);display:flex;align-items:center;justify-content:center}
.btn .arrow{background:var(--ink);width:28px;display:flex;align-items:center;justify-content:center}
.login{left:694px;top:9px;width:94px}
.login .label{flex:1;font-size:17px}
.search{left:208px;top:75px;width:564px;height:29px;background:var(--search);padding:3px;display:flex;gap:3px}
.select{width:119px;background:var(--white);font-size:9.5px;color:#777;display:flex;align-items:center;justify-content:space-between;padding-left:6px}
.select span.caret{width:18px;height:100%;background:var(--brand);display:flex;align-items:center;justify-content:center}
.search-btn{flex:1;display:flex}
.search-btn .label{flex:1;background:var(--brand);color:var(--white);font-size:12px;display:flex;align-items:center;justify-content:center}
.search-btn .arrow{width:22px;background:var(--white);display:flex;align-items:center;justify-content:center}
.offers{left:153px;top:144px;width:668px;height:79px;background:rgba(255,255,255,.75);display:flex;justify-content:space-around;align-items:center;padding:0 10px}
.offer{display:flex;align-items:center;gap:6px}
.offer .small{font-family:"Questrial",sans-serif;color:var(--brand);font-size:14px;line-height:1}
.offer .big{font-family:"Questrial",sans-serif;color:var(--ink);font-size:48px;line-height:.95}
.slider{left:457px;top:274px;display:flex;gap:1px}
.slider span{width:28px;height:29px;background:var(--ink);display:flex;align-items:center;justify-content:center}
.register{left:740px;top:289px;width:144px}
.register .label{flex:1;font-size:15px}
.content{left:87px;top:318px;width:797px;height:850px;background:var(--white)}
.section-title{left:102px;top:350px;font-size:27px;font-weight:300;color:var(--brand)}
.card{width:242px}
.card .photo{width:242px;height:103px}
.card h3{margin-top:14px;font-weight:400;font-size:16.5px;color:#222}
.card p{margin-top:6px;font-size:11.5px;line-height:16.5px;color:var(--text)}
.more-dot{display:inline-block;width:12px;height:12px;border-radius:50%;background:var(--ink);vertical-align:-2px;margin-left:4px;position:relative}
.more-dot::before,.more-dot::after{content:"";position:absolute;background:var(--white);left:3px;top:5.5px;width:6px;height:1px}
.more-dot::after{transform:rotate(90deg)}
.more-dot.light{background:var(--white)}
.more-dot.light::before,.more-dot.light::after{background:var(--band)}
.features{display:flex;gap:14px;margin-top:18px}
.feature{display:flex;align-items:center;gap:3px}
.feature .icon{width:18px;height:18px;border-radius:50%;background:var(--ink);display:flex;align-items:center;justify-content:center}
.feature .num{font-size:13px;color:var(--ink);line-height:1}
.feature .name{font-size:8.5px;color:var(--ink);line-height:1}
.band{left:104px;top:966px;width:764px;height:133px;background:var(--band);color:var(--white)}
.band h2{font-weight:400;font-size:18px;margin-top:18px}
.band p{font-size:10.5px;line-height:13px;margin-top:4px}
.band .link{font-size:10.5px;margin-top:6px}
.more{left:775px;top:1099px;width:93px}
.more .label{flex:1;font-size:16px;color:var(--ink);background:var(--brand)}
.more .arrow{width:27px}
.social{left:104px;top:1119px;display:flex;gap:2px}
.social span{width:25px;height:25px;background:var(--ink)}
.social span:first-child{background:var(--brand)}
.copy{left:205px;top:1127px;font-size:9.5px;color:#444}
.foot-links{right:87px;top:1176px;display:flex;gap:14px;font-size:10px;color:#555}
</style>
</head>
<body>
<div class="abs hero" role="img" aria-label="City skyline photograph across a harbor under a blue sky"></div>

<header class="abs header">
  <div class="abs logo">Harborline Realty</div>
  <nav class="abs nav">
    <a class="current" href="#">Home</a><a href="#">Find Property</a><a href="#">Offices</a><a href="#">Associates</a><a href="#">Contact</a>
  </nav>
  <div class="abs btn login"><span class="label">Login</span><span class="arrow"><svg width="8" height="12"><path d="M1 1l5 5-5 5" fill="none" stroke="#fff" stroke-width="2"/></svg></span></div>
</header>

<form class="abs search">
  <div class="select">City<span class="caret"><svg width="9" height="6"><path d="M1 1l3.5 4 3.5-4" fill="none" stroke="#fff" stroke-width="1.5"/></svg></span></div>
  <div class="select">Lifestyle<span class="caret"><svg width="9" height="6"><path d="M1 1l3.5 4 3.5-4" fill="none" stroke="#fff" stroke-width="1.5"/></svg></span></div>
  <div class="select">Property type<span class="caret"><svg width="9" height="6"><path d="M1 1l3.5 4 3.5-4" fill="none" stroke="#fff" stroke-width="1.5"/></svg></span></div>
  <div class="select">Price<span class="caret"><svg width="9" height="6"><path d="M1 1l3.5 4 3.5-4" fill="none" stroke="#fff" stroke-width="1.5"/></svg></span></div>
  <div class="search-btn"><span class="label">Search</span><span class="arrow"><svg width="7" height="10"><path d="M1 1l4 4-4 4" fill="none" stroke="#111" stroke-width="1.5"/></svg></span></div>
</form>

<div class="abs offers">
  <div class="offer">
    <svg width="58" height="58" viewBox="0 0 58 58"><rect x="4" y="18" width="20" height="40" fill="#1477a8"/><rect x="26" y="4" width="28" height="54" fill="#1477a8"/><g fill="#fff"><rect x="30" y="10" width="5" height="5"/><rect x="39" y="10" width="5" height="5"/><rect x="30" y="20" width="5" height="5"/><rect x="39" y="20" width="5" height="5"/><rect x="30" y="30" width="5" height="5"/><rect x="39" y="30" width="5" height="5"/><rect x="30" y="40" width="5" height="5"/><rect x="39" y="40" width="5" height="5"/><rect x="9" y="24" width="4" height="4"/><rect x="9" y="34" width="4" height="4"/><rect x="9" y="44" width="4" height="4"/></g></svg>
    <div><div class="small">PROPERTIES FOR</div><div class="big">SALE</div></div>
  </div>
  <div class="offer">
    <svg width="52" height="58" viewBox="0 0 52 58"><rect x="2" y="14" width="24" height="44" fill="#1477a8"/><rect x="28" y="28" width="20" height="30" fill="#1477a8"/><g fill="#fff"><rect x="7" y="20" width="5" height="5"/><rect x="16" y="20" width="5" height="5"/><rect x="7" y="30" width="5" height="5"/><rect x="16" y="30" width="5" height="5"/><rect x="7" y="40" width="5" height="5"/><rect x="16" y="40" width="5" height="5"/><rect x="33" y="34" width="4" height="4"/><rect x="33" y="44" width="4" height="4"/></g></svg>
    <div><div class="small">PROPERTIES FOR</div><div class="big">RENT</div></div>
  </div>
  <div class="offer">
    <svg width="60" height="58" viewBox="0 0 60 58"><rect x="2" y="24" width="16" height="34" fill="#1477a8"/><rect x="20" y="10" width="36" height="48" fill="#1477a8"/><g fill="#fff"><rect x="25" y="16" width="5" height="5"/><rect x="34" y="16" width="5" height="5"/><rect x="43" y="16" width="5" height="5"/><rect x="25" y="28" width="5" height="5"/><rect x="34" y="28" width="5" height="5"/><rect x="43" y="28" width="5" height="5"/><rect x="25" y="40" width="5" height="5"/><rect x="34" y="40" width="5" height="5"/><rect x="43" y="40" width="5" height="5"/></g></svg>
    <div><div class="small">PROPERTIES FOR</div><div class="big">LEASE</div></div>
  </div>
</div>

<div class="abs slider">
  <span><svg width="7" height="11"><path d="M6 1L1.5 5.5 6 10" fill="none" stroke="#fff" stroke-width="1.6"/></svg></span>
  <span><svg width="7" height="11"><path d="M1 1l4.5 4.5L1 10" fill="none" stroke="#fff" stroke-width="1.6"/></svg></span>
</div>
<div class="abs btn register"><span class="label">Register Now</span><span class="arrow"><svg width="8" height="12"><path d="M1 1l5 5-5 5" fill="none" stroke="#fff" stroke-width="2"/></svg></span></div>

<main class="abs content"></main>
<h1 class="abs section-title">Featured Property</h1>

<article class="abs card" style="left:104px;top:403px">
  <div class="photo" role="img" aria-label="Glass office towers against a blue sky" style="background:linear-gradient(160deg,#1d62b8,#4a8fd8 45%,#6d7c8a 75%,#8a7058)"></div>
  <h3>Nam quis ligula a nibh</h3>
  <p>Etiam non felis mi. Quisque feugiat, lectus non feugiat consectetur, purus ipsum lobortis nisl, a sollicitudin risus arcu<span class="more-dot" style="background:#1477a8"></span></p>
  <div class="features">
    <div class="feature"><span class="icon"><svg width="10" height="8"><rect x="0" y="3" width="10" height="4" fill="#fff"/><rect x="0" y="1" width="3" height="2" fill="#fff"/></svg></span><div><div class="num">1</div><div class="name">Bedroom</div></div></div>
    <div class="feature"><span class="icon"><svg width="10" height="10"><path d="M2 10V3h5v2" fill="none" stroke="#fff" stroke-width="1.5"/></svg></span><div><div class="num">1</div><div class="name">Bathroom</div></div></div>
    <div class="feature"><span class="icon"><svg width="10" height="8"><rect x="1" y="2" width="8" height="4" rx="1" fill="#fff"/></svg></span><div><div class="num">1</div><div class="name">Garage</div></div></div>
  </div>
</article>

<article class="abs card" style="left:365px;top:403px">
  <div class="photo" role="img" aria-label="White two-storey house with porch among trees" style="background:linear-gradient(180deg,#a9c4d8,#e4e4e0 45%,#6f7d55 80%,#3e5a2a)"></div>
  <h3>Nam quis ligula a nibh</h3>
  <p>Etiam non felis mi. Quisque feugiat, lectus non feugiat consectetur, purus ipsum lobortis nisl, a sollicitudin risus arcu<span class="more-dot"></span></p>
  <div class="features">
    <div class="feature"><span class="icon"><svg width="10" height="8"><rect x="0" y="3" width="10" height="4" fill="#fff"/><rect x="0" y="1" width="3" height="2" fill="#fff"/></svg></span><div><div class="num">2</div><div class="name">Bedroom</div></div></div>
    <div class="feature"><span class="icon"><svg width="10" height="10"><path d="M2 10V3h5v2" fill="none" stroke="#fff" stroke-width="1.5"/></svg></span><div><div class="num">3</div><div class="name">Bathroom</div></div></div>
    <div class="feature"><span class="icon"><svg width="10" height="8"><rect x="1" y="2" width="8" height="4" rx="1" fill="#fff"/></svg></span><div><div class="num">1</div><div class="name">Garage</div></div></div>
  </div>
</article>

<article class="abs card" style="left:625px;top:403px">
  <div class="photo" role="img" aria-label="White seaside apartment building with palm trees" style="background:linear-gradient(180deg,#4f96d6,#b8d4ec 35%,#eef0f2 60%,#5c7a4a)"></div>
  <h3>Nam quis ligula a nibh</h3>
  <p>Etiam non felis mi. Quisque feugiat, lectus non feugiat consectetur, purus ipsum lobortis nisl, a sollicitudin risus arcu<span class="more-dot"></span></p>
  <div class="features">
    <div class="feature"><span class="icon"><svg width="10" height="8"><rect x="0" y="3" width="10" height="4" fill="#fff"/><rect x="0" y="1" width="3" height="2" fill="#fff"/></svg></span><div><div class="num">2</div><div class="name">Bedroom</div></div></div>
    <div class="feature"><span class="icon"><svg width="10" height="10"><path d="M2 10V3h5v2" fill="none" stroke="#fff" stroke-width="1.5"/></svg></span><div><div class="num">2</div><div class="name">Bathroom</div></div></div>
    <div class="feature"><span class="icon"><svg width="10" height="8"><rect x="1" y="2" width="8" height="4" rx="1" fill="#fff"/></svg></span><div><div class="num">1</div><div class="name">Garage</div></div></div>
  </div>
</article>

<article class="abs card" style="left:104px;top:691px">
  <div class="photo" role="img" aria-label="Grey family house with white porch and lawn" style="background:linear-gradient(180deg,#3f5a34,#7b7f7a 40%,#d8d8d4 65%,#4d6b30)"></div>
  <h3>Nam quis ligula a nibh</h3>
  <p>Etiam non felis mi. Quisque feugiat, lectus non feugiat consectetur, purus ipsum lobortis nisl, a sollicitudin risus arcu<span class="more-dot"></span></p>
  <div class="features">
    <div class="feature"><span class="icon"><svg width="10" height="8"><rect x="0" y="3" width="10" height="4" fill="#fff"/><rect x="0" y="1" width="3" height="2" fill="#fff"/></svg></span><div><div class="num">3</div><div class="name">Bedroom</div></div></div>
    <div class="feature"><span class="icon"><svg width="10" height="10"><path d="M2 10V3h5v2" fill="none" stroke="#fff" stroke-width="1.5"/></svg></span><div><div class="num">3</div><div class="name">Bathroom</div></div></div>
    <div class="feature"><span class="icon"><svg width="10" height="8"><rect x="1" y="2" width="8" height="4" rx="1" fill="#fff"/></svg></span><div><div class="num">2</div><div class="name">Garage</div></div></div>
  </div>
</article>

<article class="abs card" style="left:365px;top:691px">
  <div class="photo" role="img" aria-label="Beige suburban house with gables and front garden" style="background:linear-gradient(180deg,#8fb0cc,#9c8f7a 35%,#cfc6b4 60%,#4f6a34)"></div>
  <h3>Nam quis ligula a nibh</h3>
  <p>Etiam non felis mi. Quisque feugiat, lectus non feugiat consectetur, purus ipsum lobortis nisl, a sollicitudin risus arcu<span class="more-dot"></span></p>
  <div class="features">
    <div class="feature"><span class="icon"><svg width="10" height="8"><rect x="0" y="3" width="10" height="4" fill="#fff"/><rect x="0" y="1" width="3" height="2" fill="#fff"/></svg></span><div><div class="num">3</div><div class="name">Bedroom</div></div></div>
    <div class="feature"><span class="icon"><svg width="10" height="10"><path d="M2 10V3h5v2" fill="none" stroke="#fff" stroke-width="1.5"/></svg></span><div><div class="num">3</div><div class="name">Bathroom</div></div></div>
    <div class="feature"><span class="icon"><svg width="10" height="8"><rect x="1" y="2" width="8" height="4" rx="1" fill="#fff"/></svg></span><div><div class="num">2</div><div class="name">Garage</div></div></div>
  </div>
</article>

<article class="abs card" style="left:625px;top:691px">
  <div class="photo" role="img" aria-label="Stone and brick house with dark roof" style="background:linear-gradient(180deg,#c9d6e0,#6d5a4e 35%,#9a8a78 65%,#56683e)"></div>
  <h3>Nam quis ligula a nibh</h3>
  <p>Etiam non felis mi. Quisque feugiat, lectus non feugiat consectetur, purus ipsum lobortis nisl, a sollicitudin risus arcu<span class="more-dot"></span></p>
  <div class="features">
    <div class="feature"><span class="icon"><svg width="10" height="8"><rect x="0" y="3" width="10" height="4" fill="#fff"/><rect x="0" y="1" width="3" height="2" fill="#fff"/></svg></span><div><div class="num">2</div><div class="name">Bedroom</div></div></div>
    <div class="feature"><span class="icon"><svg width="10" height="10"><path d="M2 10V3h5v2" fill="none" stroke="#fff" stroke-width="1.5"/></svg></span><div><div class="num">3</div><div class="name">Bathroom</div></div></div>
    <div class="feature"><span class="icon"><svg width="10" height="8"><rect x="1" y="2" width="8" height="4" rx="1" fill="#fff"/></svg></span><div><div class="num">1</div><div class="name">Garage</div></div></div>
  </div>
</article>

<section class="abs band">
  <div class="abs" style="left:20px;top:0;width:230px">
    <h2>News</h2>
    <p>Mauris vel volutpat leo. Nunc non justo nunc. Donec sapien arcu, egestas at facilisis et, interdum eget mauris.</p>
    <div class="link">Read the full story <span class="more-dot light"></span></div>
  </div>
  <div class="abs" style="left:274px;top:0;width:475px">
    <h2>What Our Client Say</h2>
    <p>Mauris vel volutpat leo. Nunc non justo nunc. Donec sapien arcu, egestas at facilisis et, interdum eget mauris. vitae bibendum mauris. Vestibulum vehicula posuere hendrerit. risus vestibulum auctor. In hac habitasse platea dictumst.</p>
    <div class="link">More tesimonials <span class="more-dot light"></span></div>
  </div>
</section>
<div class="abs btn more"><span class="label">More</span><span class="arrow"><svg width="10" height="10"><path d="M5 0v10M0 5h10" stroke="#1477a8" stroke-width="1.3"/></svg></span></div>

<div class="abs social" aria-label="Social links"><span></span><span></span><span></span></div>
<div class="abs copy">Copyright Harborline Realty 2013.All Rights Reserved.</div>

<footer class="abs foot-links"><span>Terms</span><span>Privacy</span><span>Contact</span></footer>
</body>
</html>
```